nuvela dead see mud mask label design

Hi
looking for a nice label design for dead see mud mask for tolsa beuty here is how other poepl are labeling it https://www.shopkarvio.com/TOP-Mineral-Clay-Face-Pack/dp/Q93RMZWLPK/ref=sr_1_1_a_it?ie=UTF8&qid=1582046917&sr=8-1&keywords=dead+see+mud+mask
we attached are logo and the label from the mfr we want the colors on the albel gray and purple

```html
<!DOCTYPE html>
<html lang="en">
<head>
<meta charset="utf-8">
<title>nuvela Dead Sea Mud Mask Label</title>
<link rel="stylesheet" href="https://fonts.googleapis.com/css2?family=Lato:wght@700;900&display=swap">
<style>
  :root {
    --label-purple: #ad739f;
    --ink: #231f20;
    --title-white: #ffffff;
    --page: #ffffff;
  }
  html, body {
    margin: 0;
    padding: 0;
    width: 1200px;
    height: 754px;
    overflow: hidden;
    background: var(--page);
  }
  .label {
    position: relative;
    width: 1200px;
    height: 754px;
    background: var(--label-purple);
    border-radius: 36px;
    font-family: "Lato", Arial, sans-serif;
    color: var(--ink);
  }
  .brand {
    position: absolute;
    top: 54px;
    left: 0;
    width: 100%;
    height: 136px;
    display: flex;
    justify-content: center;
    align-items: center;
    gap: 60px;
  }
  .brand-mark {
    flex: none;
    width: 128px;
    height: 128px;
    border-radius: 50%;
    background: var(--ink);
  }
  .brand-name {
    font-weight: 700;
    font-size: 120px;
    line-height: 1;
    color: var(--ink);
    padding-bottom: 16px;
  }
  .product-title {
    position: absolute;
    top: 322px;
    left: 0;
    width: 100%;
    margin: 0;
    text-align: center;
    font-weight: 700;
    font-size: 90px;
    line-height: 1;
    color: var(--title-white);
    letter-spacing: 0.5px;
  }
  .claims {
    position: absolute;
    top: 555px;
    left: 0;
    width: 100%;
    margin: 0;
    text-align: center;
    font-weight: 700;
    font-size: 34px;
    line-height: 43px;
    letter-spacing: 0.6px;
  }
  .net-weight {
    position: absolute;
    top: 680px;
    left: 0;
    width: 100%;
    margin: 0;
    text-align: center;
    font-weight: 700;
    font-size: 34px;
    line-height: 1;
    letter-spacing: 0.6px;
  }
</style>
</head>
<body>
  <main class="label">
    <header class="brand">
      <span class="brand-mark" aria-hidden="true"></span>
      <span class="brand-name">nuvela</span>
    </header>
    <h1 class="product-title">Dead Sea Mud Mask</h1>
    <p class="claims">
      100% Natural Mineral-Infused derived form the Dead Sea<br>
      Deep Skin Cleanser, Pore Reducer &amp; Helps Clear Acne
    </p>
    <p class="net-weight">259 grams | 8.8 fl. oz</p>
  </main>
</body>
</html>
```